Brightfold Systems
Business Card
Professional
Daniel Harcourt
Serious Games Specialist
52 Millbrook Lane Arnprior, Ontario K7S 2B9 Canada
d.harcourt@brightfoldsys.net
http://www.brightfoldsys.net
Our company designs, operates, and supports "Serious Games" for training military, law enforcement, and government. We would like our business card to reflect this audience while maintaining the "cool" and "edgy" side of video games.
Feel the Brightfold.

```html
<!DOCTYPE html>
<html lang="en">
<head>
<meta charset="utf-8">
<title>Brightfold Systems — Business Card</title>
<link href="https://fonts.googleapis.com/css2?family=Open+Sans:wght@400;600;700&display=swap" rel="stylesheet">
<style>
  :root {
    --bg: #e9e6e1;
    --card: #ffffff;
    --brand-blue: #1f5fae;
    --deep-blue: #173e78;
    --text-grey: #5a5f66;
    --shadow: rgba(0, 0, 0, 0.18);
  }
  * { box-sizing: border-box; margin: 0; padding: 0; }
  html, body {
    width: 1200px; height: 646px; overflow: hidden;
    background: var(--bg);
    font-family: "Open Sans", Arial, sans-serif;
  }
  .canvas {
    width: 1200px; height: 646px;
    display: flex; align-items: center; justify-content: center; gap: 60px;
  }
  .card {
    width: 520px; height: 297px;
    background: var(--card);
    box-shadow: 0 10px 28px var(--shadow);
    position: relative;
    overflow: hidden;
  }
  .wordmark {
    display: flex; align-items: center; gap: 14px;
  }
  .wordmark-dot {
    width: 40px; height: 40px; border-radius: 50%;
    background: var(--brand-blue); flex: none;
  }
  .wordmark-name {
    font-size: 30px; font-weight: 700; color: var(--deep-blue);
    letter-spacing: 0.5px; white-space: nowrap;
  }
  /* Front */
  .card-front .wordmark { position: absolute; left: 56px; top: 62px; }
  .contact {
    position: absolute; left: 56px; top: 160px;
    font-size: 12.5px; color: var(--text-grey); line-height: 1.9;
    list-style: none;
  }
  .contact li { display: flex; align-items: center; gap: 9px; white-space: nowrap; }
  .contact svg { width: 13px; height: 13px; flex: none; }
  .contact .address { padding-left: 22px; margin-bottom: 4px; }
  /* Back */
  .card-back .wordmark { position: absolute; left: 48px; top: 126px; }
  .card-back .wordmark-name { font-size: 24px; }
  .card-back .wordmark-dot { width: 34px; height: 34px; }
  .person {
    position: absolute; left: 262px; top: 118px;
  }
  .person-name {
    font-size: 21px; font-weight: 600; color: var(--brand-blue);
    white-space: nowrap;
  }
  .person-title {
    font-size: 13px; color: var(--text-grey); margin-top: 2px;
    letter-spacing: 0.4px; white-space: nowrap;
  }
</style>
</head>
<body>
<main class="canvas">
  <section class="card card-front" aria-label="Card front">
    <div class="wordmark">
      <span class="wordmark-dot"></span>
      <span class="wordmark-name">Brightfold Systems</span>
    </div>
    <ul class="contact">
      <li class="address">52 Millbrook Lane Cedarvale, Northshire N0X 2B9 Canada</li>
      <li>
        <svg viewBox="0 0 24 24" aria-hidden="true"><path fill="#1f5fae" d="M6.6 10.8a15.1 15.1 0 0 0 6.6 6.6l2.2-2.2c.3-.3.7-.4 1-.2 1.1.4 2.3.6 3.6.6.6 0 1 .4 1 1V20c0 .6-.4 1-1 1A17 17 0 0 1 3 4c0-.6.4-1 1-1h3.5c.6 0 1 .4 1 1 0 1.3.2 2.5.6 3.6.1.3 0 .7-.2 1z"/></svg>
        613-555-0148
      </li>
      <li>
        <svg viewBox="0 0 24 24" aria-hidden="true"><path d="M3 5h18v14H3z M3 5l9 7 9-7" fill="none" stroke="#1f5fae" stroke-width="2"/></svg>
        d.harcourt@brightfoldsys.net
      </li>
      <li>
        <svg viewBox="0 0 24 24" aria-hidden="true"><circle cx="12" cy="12" r="9" fill="none" stroke="#1f5fae" stroke-width="2"/><path d="M3 12h18M12 3c3 3 3 15 0 18M12 3c-3 3-3 15 0 18" fill="none" stroke="#1f5fae" stroke-width="1.6"/></svg>
        http://www.brightfoldsys.net
      </li>
    </ul>
  </section>

  <section class="card card-back" aria-label="Card back">
    <div class="wordmark">
      <span class="wordmark-dot"></span>
      <span class="wordmark-name">Brightfold</span>
    </div>
    <div class="person">
      <p class="person-name">Daniel Harcourt</p>
      <p class="person-title">Serious Games Specialist</p>
    </div>
  </section>
</main>
</body>
</html>
```